Post Card Design Bright Lantern Youth

We need a postcard design that will be mailed to all residents offering free pickups of donated clothing. Our foundation is called Bright Lantern Youth, we are a nonprofit charitable organization that provides meals and medical services to children in need in Honduras. Collecting unwanted second-hand clothing generates revenue that helps fund the mission and programs run by our foundation. We would like to offer our pickup services to everyone who has any unwanted reusable clothing.

```html
<!DOCTYPE html>
<html lang="en">
<head>
<meta charset="utf-8">
<title>Bright Lantern Youth – Free Clothing Pickup Postcard</title>
<link rel="stylesheet" href="https://fonts.googleapis.com/css2?family=Delius+Unicase:wght@400;700&family=Fredoka:wght@500;600;700&family=Nunito:wght@500;600;700;800&display=swap">
<style>
  :root {
    --page: #ececec;
    --card: #ffffff;
    --pink: #e6198a;
    --blue: #1b9ad9;
    --yellow: #f7d21c;
    --green: #7cc242;
    --lime: #b5d334;
    --ink: #3d4650;
    --muted: #9aa1a8;
    --sky-top: #a9cdea;
    --sky-low: #e9f2f8;
  }
  * { box-sizing: border-box; margin: 0; padding: 0; }
  html, body { width: 1200px; height: 1200px; overflow: hidden; }
  body { background: var(--page); font-family: "Nunito", sans-serif; position: relative; }

  .postcard {
    position: absolute; left: 213px; width: 774px; height: 515px;
    background: var(--card); overflow: hidden;
    box-shadow: 0 2px 6px rgba(0,0,0,.18);
  }
  .postcard--front { top: 70px; }
  .postcard--back { top: 622px; }
  .abs { position: absolute; }
  svg.abs { display: block; }

  /* front */
  .scene-photo {
    left: 0; top: 0; width: 774px; height: 515px;
    background: linear-gradient(180deg, var(--sky-top) 0%, var(--sky-low) 55%, #d9d4d2 100%);
  }
  .child-photo {
    left: 245px; top: 300px; width: 200px; height: 215px; border-radius: 50% 50% 0 0;
    background: radial-gradient(ellipse at 50% 60%, #b7a8a6 0%, #8f96a8 60%, rgba(143,150,168,0) 100%);
  }
  .headline-ask {
    left: 32px; top: 18px; font-family: "Delius Unicase", cursive; color: #fff; line-height: 1;
  }
  .headline-ask .lead { color: var(--yellow); font-size: 46px; display: block; line-height: .95; }
  .headline-ask .rest { font-size: 33px; display: block; line-height: .95; margin-top: 12px; }

  .brand-badge {
    width: 146px; height: 146px; border-radius: 50%; background: #fff;
    border: 5px solid var(--blue);
    display: flex; align-items: center; justify-content: center; text-align: center;
    font-family: "Delius Unicase", cursive; font-weight: 700; color: var(--green);
    font-size: 18px; line-height: 1.1; padding: 0 14px;
  }
  .brand-badge--front { left: 38px; top: 206px; }
  .brand-badge--back { left: 432px; top: 32px; width: 156px; height: 156px; font-size: 19px; }

  .band-label {
    font-family: "Delius Unicase", cursive; color: #fff; font-size: 26px; white-space: nowrap;
  }
  .contact-list { list-style: none; color: var(--ink); font-size: 16px; line-height: 1.32; font-weight: 600; white-space: nowrap; }
  .contact-list li { display: flex; align-items: flex-start; gap: 8px; }
  .contact-list svg { flex: none; margin-top: 3px; }
  .contact-list .indent { padding-left: 24px; }
  .contact-list .web { color: var(--blue); font-weight: 800; font-size: 21px; padding-left: 24px; }

  .offer-pill {
    left: 460px; top: 11px; width: 165px; height: 30px; border-radius: 15px;
    background: var(--blue); border: 2px solid #fff; color: #fff;
    font-family: "Delius Unicase", cursive; font-size: 20px; text-align: center; line-height: 26px;
  }
  .offer-title { left: 335px; top: 44px; width: 420px; text-align: center; }
  .offer-title .big { font-family: "Fredoka", sans-serif; font-weight: 700; font-size: 55px; line-height: 1; letter-spacing: .5px; white-space: nowrap; }
  .offer-title .pink { color: var(--pink); }
  .offer-title .blue { color: var(--blue); }
  .offer-title .sub { font-family: "Delius Unicase", cursive; color: var(--ink); font-size: 30px; line-height: 1.05; display: block; white-space: nowrap; }
  .dots { border-top: 3px dotted currentColor; }
  .offer-title .dots { width: 350px; margin: 6px auto 0; color: var(--green); }
  .offer-text { left: 355px; top: 146px; width: 380px; text-align: center; color: var(--ink); font-size: 17px; font-weight: 600; line-height: 1.2; }

  .difference { left: 450px; top: 426px; width: 316px; text-align: center; color: #fff; }
  .difference .label { font-family: "Delius Unicase", cursive; font-size: 21px; display: block; white-space: nowrap; }
  .difference .dots { width: 250px; margin: 3px auto 5px; color: #fff; }
  .difference .note { font-size: 17px; font-weight: 700; line-height: 1.15; }

  /* back */
  .back-tab { left: 24px; top: 20px; }
  .about-text { left: 22px; top: 104px; color: #fff; font-size: 18.5px; font-weight: 600; line-height: 1.16; }
  .volunteer-photo {
    left: 238px; top: 180px; width: 316px; height: 316px; border-radius: 50%;
    border: 5px solid var(--green);
    background: radial-gradient(circle at 55% 35%, #d6dfc8 0%, #a9b99a 45%, #6f6c66 100%);
  }
  .social-dot { width: 40px; height: 40px; border-radius: 50%; background: var(--green); border: 3px solid #fff; }
</style>
</head>
<body>

<section class="postcard postcard--front" aria-label="Postcard front">
  <div class="abs scene-photo" role="img" aria-label="Photo of blue sky with flying clothes and a pickup truck on a road"></div>

  <svg class="abs" style="left:0;top:0" width="774" height="515" viewBox="0 0 774 515" aria-hidden="true">
    <path d="M0 0 H277 C300 110 318 250 300 352 H0 Z" fill="var(--pink)"/>
    <path d="M0 352 H240 V402 C230 410 220 410 210 402 C200 394 190 394 180 402 C170 410 160 410 150 402 C140 394 130 394 120 402 C110 410 100 410 90 402 C80 394 70 394 60 402 C50 410 40 410 30 402 C20 394 10 394 0 402 Z" fill="var(--blue)"/>
    <path d="M0 402 C10 394 20 394 30 402 C40 410 50 410 60 402 C70 394 80 394 90 402 C100 410 110 410 120 402 C130 394 140 394 150 402 C160 410 170 410 180 402 C190 394 200 394 210 402 C220 410 230 410 240 402 V515 H0 Z" fill="#fff"/>
    <defs>
      <linearGradient id="diffGrad" x1="0" y1="0" x2="1" y2="0">
        <stop offset="0" stop-color="var(--green)"/>
        <stop offset=".6" stop-color="var(--lime)"/>
        <stop offset="1" stop-color="var(--yellow)"/>
      </linearGradient>
    </defs>
    <path d="M380 515 C420 440 490 400 774 385 V515 Z" fill="url(#diffGrad)"/>
  </svg>

  <div class="abs child-photo" role="img" aria-label="Photo of a child carrying a big pile of clothes"></div>

  <h1 class="abs headline-ask">
    <span class="lead">DO YOU<br>have</span>
    <span class="rest">unwanted<br>reusable<br>CLOTHING?</span>
  </h1>

  <div class="abs brand-badge brand-badge--front">Bright Lantern Youth</div>

  <div class="abs band-label" style="left:28px;top:360px">CONTACT US</div>
  <ul class="abs contact-list" style="left:14px;top:419px">
    <li><svg width="14" height="18" viewBox="0 0 14 18"><path d="M7 0a7 7 0 0 0-7 7c0 5 7 11 7 11s7-6 7-11a7 7 0 0 0-7-7zm0 10a3 3 0 1 1 0-6 3 3 0 0 1 0 6z" fill="var(--muted)"/></svg>12 Maple Grove Rd.</li>
    <li class="indent">Brookdale, NJ 07099</li>
    <li><svg width="16" height="16" viewBox="0 0 16 16"><path d="M3.5 1l3 3-1.8 2a9 9 0 0 0 5.3 5.3l2-1.8 3 3-2 2.5C7 15 1 9 1 3z" fill="var(--muted)"/></svg>(201) 555-0147</li>
    <li><svg width="16" height="12" viewBox="0 0 16 12"><rect width="16" height="12" rx="1" fill="var(--muted)"/><path d="M1 1l7 6 7-6" stroke="#fff" stroke-width="1.5" fill="none"/></svg>Info@brightlantern.org</li>
  </ul>

  <div class="abs offer-pill">we offer</div>
  <h2 class="abs offer-title">
    <span class="big"><span class="pink">FREE</span> <span class="blue">PICKUPS</span></span>
    <span class="sub">OF DONATED CLOTHING</span>
    <div class="dots"></div>
  </h2>
  <p class="abs offer-text">We would like to offer our pickup services<br>to everyone who has any unwanted<br>reusable clothing.</p>

  <div class="abs difference">
    <span class="label">LET'S MAKE A DIFFERENCE</span>
    <div class="dots"></div>
    <p class="note">Bringing Reusable Clothing<br>to Communities in Need</p>
  </div>
</section>

<section class="postcard postcard--back" aria-label="Postcard back">
  <svg class="abs" style="left:0;top:0" width="774" height="515" viewBox="0 0 774 515" aria-hidden="true">
    <path d="M0 17 H418 L447 64 H0 Z" fill="var(--pink)"/>
    <path d="M0 70 C10 62 20 62 30 70 C40 78 50 78 60 70 C70 62 80 62 90 70 C100 78 110 78 120 70 C130 62 140 62 150 70 C160 78 170 78 180 70 C190 62 200 62 210 70 C220 78 230 78 240 70 C250 62 260 62 270 70 C280 78 290 78 300 70 C310 62 320 62 330 70 C340 78 350 78 360 70 C370 62 380 62 390 70 C400 78 410 78 424 70 V334 H0 Z" fill="var(--blue)"/>
    <path d="M0 334 H235 V386 H0 Z" fill="var(--yellow)"/>
  </svg>

  <div class="abs band-label back-tab">LET'S MAKE A DIFFERENCE!</div>
  <div class="abs brand-badge brand-badge--back">Bright Lantern Youth</div>

  <p class="abs about-text">We are a nonprofit charitable organization<br>that provides meals and medical services<br>to children in need in Honduras.<br>Collecting unwanted<br>second-hand clothing<br>generates revenue<br>that helps fund the<br>mission and programs<br>run by our foundation.</p>

  <div class="abs volunteer-photo" role="img" aria-label="Photo of a volunteer handing donated clothes to children"></div>

  <div class="abs band-label" style="left:24px;top:341px">CONTACT US</div>
  <ul class="abs contact-list" style="left:14px;top:392px">
    <li><svg width="14" height="18" viewBox="0 0 14 18"><path d="M7 0a7 7 0 0 0-7 7c0 5 7 11 7 11s7-6 7-11a7 7 0 0 0-7-7zm0 10a3 3 0 1 1 0-6 3 3 0 0 1 0 6z" fill="var(--muted)"/></svg>12 Maple Grove Rd.</li>
    <li class="indent">Brookdale, NJ 07099</li>
    <li><svg width="16" height="16" viewBox="0 0 16 16"><path d="M3.5 1l3 3-1.8 2a9 9 0 0 0 5.3 5.3l2-1.8 3 3-2 2.5C7 15 1 9 1 3z" fill="var(--muted)"/></svg>(201) 555-0147</li>
    <li><svg width="16" height="12" viewBox="0 0 16 12"><rect width="16" height="12" rx="1" fill="var(--muted)"/><path d="M1 1l7 6 7-6" stroke="#fff" stroke-width="1.5" fill="none"/></svg>Info@brightlantern.org</li>
    <li class="web">brightlantern.org</li>
  </ul>

  <div class="abs social-dot" style="left:252px;top:425px"></div>
  <div class="abs social-dot" style="left:288px;top:456px"></div>
</section>

</body>
</html>
```